Cordial Keys

We teach men how to be successful with women.

We will be putting an Vidhostly on the page.

We want to push men to take our 12 month learning program.

Open to ideas and layouts. The website will also be a landing page for our TV campaign.

Cordial keys is a company that will be marketing as an infomercial on late night television and via the internet. 

We will be selling a 12 month program for $997 (paid monthly). It will teach men how to get the woman of their dreams and how attraction is not a choice.
We have systematically developed a program for helping men attract women. 
We do have some competitors but they in the pickup commuinity (Hob Board, Greg Tolliver and Quillon Methods are all competitors.
Our website name is cordialkeys.com.au.
We will be having an vidhostly.com.au on our website to aid the process on making the sale.

The program will be an e-learning program that will be purchased over 12 months.

We also will be selling boot camps in which guys go for a week at a time and train to refine their skills.

Tv

```html
<!DOCTYPE html>
<html lang="en">
<head>
<meta charset="utf-8">
<title>Cordial Keys</title>
<link href="https://fonts.googleapis.com/css2?family=Roboto:wght@300;400;500;700&family=Roboto+Condensed:wght@700&display=swap" rel="stylesheet">
<style>
:root{
  --magenta:#cc0b8b;
  --teal:#5bbfcc;
  --yellow:#d9d600;
  --brown:#4a1e14;
  --ink:#222;
  --text:#333;
  --muted:#9a9a9a;
  --nav:#666;
  --band:#f2f2f2;
  --rule:#999;
  --blue:#1f7fd8;
}
*{margin:0;padding:0;box-sizing:border-box}
html,body{width:1200px;height:1178px;overflow:hidden;background:#fff}
body{position:relative;font-family:'Roboto',sans-serif;color:var(--text)}
.abs{position:absolute}
.topbar{left:0;top:0;width:1200px;height:15px;background:#000}
.account{right:107px;top:0;font-size:13px;line-height:15px;color:#fff}
.header-band{left:0;top:15px;width:1200px;height:168px;background:var(--band)}
.brand{left:118px;top:28px;display:flex;align-items:center;gap:14px}
.brand-mark{width:40px;height:40px;background:var(--magenta)}
.brand-name{font-size:48px;font-weight:300;color:var(--ink);letter-spacing:1px}
.nav{top:108px;left:574px;display:flex;font-size:18px;color:var(--nav);white-space:nowrap}
.nav span.sep{margin:0 12px}
.stage{left:152px;top:147px;width:910px;height:360px;background:#fff}
.photo{position:absolute}
.tag{position:absolute;font-family:'Roboto Condensed',sans-serif;font-weight:700;font-size:30px;line-height:42px;padding-left:20px;white-space:nowrap}
.badge{left:1008px;top:460px}
.section-title{left:0;width:1228px;top:538px;text-align:center;font-size:30px;color:var(--ink)}
.dots{height:0;border-top:1px dotted var(--magenta)}
.pin{width:8px;height:8px;border-radius:50%;background:var(--magenta)}
.feature{top:588px;width:240px}
.feature .icon{width:52px;height:52px;border-radius:50%;margin-bottom:20px;display:flex;align-items:center;justify-content:center}
.feature h3{font-weight:400;font-size:20px;color:var(--text);margin-bottom:8px;white-space:nowrap}
.feature p{font-size:14px;line-height:18px;color:var(--muted);font-weight:300;height:90px}
.feature .more{font-size:14px;color:var(--muted);font-weight:300}
.divider{left:115px;top:825px;width:973px;border-top:1px dotted #555}
.block-title{font-size:20px;color:var(--text)}
.video{left:118px;top:896px;width:246px;height:153px;background:#333;padding:7px}
.video-frame{width:100%;height:100%;background:linear-gradient(135deg,#9a9a9a,#d6d6d6 55%,#8c8c8c)}
.play{left:97px;top:52px;width:44px;height:47px;background:rgba(235,235,235,.85)}
.quote{left:415px;top:900px;width:390px;font-size:14px;line-height:20px;color:#aaa;font-weight:300}
.quote-mark{left:402px;top:882px;font-size:62px;line-height:62px;color:#999;font-family:Georgia,serif}
.quote-more{left:419px;top:1037px;font-size:14px;color:#555}
.thumb{width:119px;height:73px}
.social{width:48px;height:48px;border-radius:50%;border:2px solid #2a4a7a;display:flex;align-items:center;justify-content:center;font-size:8px;color:#2a4a7a;font-weight:500}
.footer-rule{left:341px;width:758px;height:0;border-top:1px solid #aaa}
.footer-links{left:376px;top:1123px;font-size:11px;color:#111;white-space:nowrap}
.footer-links .sep{margin:0 7px}
.copyright{right:122px;top:1124px;font-size:10px;color:#444}
</style>
</head>
<body>
<div class="abs topbar"></div>
<div class="abs account">Login &nbsp;I&nbsp; Registration</div>
<div class="abs header-band"></div>

<div class="abs brand">
  <div class="brand-mark"></div>
  <div class="brand-name">Cordial keys</div>
</div>

<nav class="abs nav">
  <span>Home</span><span class="sep">|</span>
  <span>About us</span><span class="sep">|</span>
  <span>Learning system</span><span class="sep" style="margin:0 18px">|</span>
  <span>Help</span><span class="sep">|</span>
  <span>Contact us</span>
</nav>

<div class="abs stage"></div>

<div class="photo" role="img" aria-label="Smiling couple close together" style="left:161px;top:160px;width:209px;height:338px;background:linear-gradient(120deg,#f6eee8,#d9b39a 50%,#f3e8e0)"></div>
<div class="photo" role="img" aria-label="Happy young couple in summer clothes" style="left:388px;top:207px;width:209px;height:291px;background:linear-gradient(135deg,#c9a888,#e6c2a2 45%,#a2876a)"></div>
<div class="photo" role="img" aria-label="Laughing man with woman kissing his cheek" style="left:615px;top:160px;width:209px;height:287px;background:linear-gradient(135deg,#c6c04a,#e2b98f 50%,#9fa23a)"></div>
<div class="photo" role="img" aria-label="Couple kissing in warm sunlight" style="left:840px;top:160px;width:209px;height:338px;background:linear-gradient(135deg,#d9a04a,#f1d3a9 55%,#f7efe2)"></div>

<div class="tag" style="left:339px;top:162px;width:188px;height:43px;background:var(--teal);color:var(--ink)">/ men how</div>
<div class="tag" style="left:906px;top:155px;width:193px;height:42px;background:var(--brown);color:#fff;padding-left:8px">/ with women</div>
<div class="tag" style="left:102px;top:456px;width:188px;height:42px;background:var(--yellow);color:var(--ink)">/ We teach</div>
<div class="tag" style="left:562px;top:456px;width:262px;height:42px;background:var(--magenta);color:var(--ink);padding-left:12px">/ to be successful</div>

<svg class="abs badge" width="88" height="88" viewBox="0 0 88 88" aria-label="Special offer">
  <polygon fill="var(--blue)" points="44,2 50,10 59,5 62,15 72,13 72,23 82,25 78,34 86,40 79,47 84,56 75,59 76,69 66,69 63,79 54,75 48,84 41,77 33,83 29,74 19,76 19,66 9,64 13,55 4,49 11,42 5,34 14,30 12,20 22,19 24,9 33,12 37,3"/>
  <text x="44" y="42" text-anchor="middle" font-family="Roboto Condensed, sans-serif" font-weight="700" font-size="15" fill="#fff">SPECIAL</text>
  <text x="44" y="57" text-anchor="middle" font-family="Roboto Condensed, sans-serif" font-weight="700" font-size="15" fill="#fff">OFFER</text>
</svg>

<div class="abs pin" style="left:122px;top:552px"></div>
<div class="abs dots" style="left:130px;top:556px;width:313px"></div>
<h2 class="abs section-title" style="font-weight:400">How we can help you</h2>
<div class="abs dots" style="left:775px;top:559px;width:287px"></div>
<div class="abs pin" style="left:1062px;top:555px"></div>

<div class="abs feature" style="left:116px">
  <div class="icon" style="background:var(--magenta);margin-left:77px">
    <svg width="20" height="30" viewBox="0 0 20 30"><circle cx="10" cy="4" r="3.5" fill="#fff"/><rect x="5" y="9" width="10" height="11" rx="2" fill="#fff"/><rect x="6.5" y="19" width="3" height="10" fill="#fff"/><rect x="10.5" y="19" width="3" height="10" fill="#fff"/></svg>
  </div>
  <h3 style="padding-left:46px">How we began</h3>
  <p>Lorem ipsum dolor sit amet, con-sectetuer adipiscing elit. Aenean commodo ligula eget dolor. Aenean massa. Cum sociis natoque penati</p>
  <div class="more">view more &gt;</div>
</div>

<div class="abs feature" style="left:371px">
  <div class="icon" style="background:var(--yellow);margin-left:65px">
    <svg width="24" height="24" viewBox="0 0 24 24"><rect x="3" y="3" width="18" height="18" fill="#eee"/><path d="M7 17 L17 6" stroke="#888" stroke-width="2"/></svg>
  </div>
  <h3 style="padding-left:17px">Learning program</h3>
  <p>Lorem ipsum dolor sit amet, con-sectetuer adipiscing elit.<br>Aenean Aenean massa. Cum sociis natoque penati</p>
  <div class="more">view more &gt;</div>
</div>

<div class="abs feature" style="left:631px">
  <div class="icon" style="background:var(--teal);margin-left:72px">
    <svg width="30" height="28" viewBox="0 0 30 28"><rect x="3" y="6" width="19" height="19" fill="none" stroke="#fff" stroke-width="2.5"/><path d="M8 15 L13 20 L27 3" fill="none" stroke="#fff" stroke-width="3.5"/></svg>
  </div>
  <h3 style="padding-left:62px">Our Work</h3>
  <p>Lorem ipsum dolor sit amet, con commodo ligula eget dolor. Aenean massa. Cum sociis natoque penati</p>
  <div class="more">view more &gt;</div>
</div>

<div class="abs feature" style="left:884px">
  <div class="icon" style="background:var(--brown);margin-left:62px;width:56px;height:56px;margin-top:-2px;margin-bottom:18px">
    <svg width="28" height="20" viewBox="0 0 28 20"><rect x="1" y="1" width="26" height="18" fill="none" stroke="#fff" stroke-width="2"/><path d="M1 1 L14 11 L27 1 M1 19 L11 9 M27 19 L17 9" fill="none" stroke="#fff" stroke-width="2"/></svg>
  </div>
  <h3 style="padding-left:31px">Get in touch</h3>
  <p>Lorem ipsum dolor sit amet, con commodo ligula eget dolor. Aenean massa. Cum sociis na-toque penati</p>
  <div class="more">view more &gt;</div>
</div>

<div class="abs divider"></div>

<svg class="abs" style="left:116px;top:852px" width="38" height="29" viewBox="0 0 38 29"><rect x="2" y="2" width="34" height="25" fill="none" stroke="#111" stroke-width="4"/><rect x="11" y="10" width="16" height="9" fill="#111"/></svg>
<div class="abs block-title" style="left:168px;top:855px">Latest Video</div>
<div class="abs video">
  <div class="video-frame" role="img" aria-label="Video still of a relaxed woman"></div>
  <div class="abs play"><svg width="44" height="47" viewBox="0 0 44 47"><polygon points="14,12 33,23.5 14,35" fill="#777"/></svg></div>
</div>

<svg class="abs" style="left:388px;top:845px" width="32" height="36" viewBox="0 0 32 36"><path d="M2 2 L7 1 L30 32 L28 35 Z" fill="#111"/></svg>
<div class="abs block-title" style="left:421px;top:855px">Testimonials</div>
<div class="abs quote-mark">&ldquo;</div>
<p class="abs quote">&nbsp;&nbsp;&nbsp;&nbsp;&nbsp;&nbsp;Lorem ipsum dolor sit amet, scetuer adipiscing elit. Aenean commodo ligula eget dolor. Aenean massa. Cum sociis natoque &nbsp;&nbsp;&nbsp;penatibus et magnis dis &nbsp;nascetur ridiculus mus. Donec quam felis, ultricies nec, pellentesque eu, pretium quis, sem. Nulla cquatmassa quis enim.&rdquo;</p>
<div class="abs quote-more">more</div>

<svg class="abs" style="left:813px;top:852px" width="36" height="36" viewBox="0 0 36 36"><circle cx="18" cy="18" r="11" fill="none" stroke="#111" stroke-width="1.5"/><circle cx="18" cy="18" r="5" fill="#111"/><path d="M18 0 V36 M0 18 H36" stroke="#111" stroke-width="1.2"/></svg>
<div class="abs block-title" style="left:858px;top:856px">Gallery</div>
<div class="abs thumb" role="img" aria-label="Couple smiling together" style="left:822px;top:895px;background:linear-gradient(135deg,#7a8f5e,#d7ac8c 50%,#5d4a3a)"></div>
<div class="abs thumb" role="img" aria-label="Couple laughing at dinner" style="left:950px;top:895px;background:linear-gradient(135deg,#6b3a22,#d9a782 50%,#3a2418)"></div>
<div class="abs thumb" role="img" aria-label="Close portrait of a happy couple" style="left:822px;top:978px;background:linear-gradient(135deg,#c46b4a,#efc3a4 50%,#b05c3e)"></div>
<div class="abs thumb" role="img" aria-label="Couple sharing a drink" style="left:950px;top:978px;background:linear-gradient(135deg,#2e1d14,#c9936d 50%,#1f140e)"></div>

<div class="abs social" style="left:128px;top:1105px">Friendnet</div>
<div class="abs social" style="left:190px;top:1105px">Searchly</div>
<div class="abs social" style="left:255px;top:1105px">Clipstream</div>

<div class="abs footer-rule" style="top:1115px"></div>
<div class="abs footer-links">Home<span class="sep">|</span>About<span class="sep">|</span>FAQ<span class="sep">|</span>Terms<span class="sep">|</span>Privacy<span class="sep">|</span>Contact</div>
<div class="abs copyright">Copyright &copy; 2012 cordialkeys.com All rights reserved.</div>
<div class="abs footer-rule" style="top:1143px"></div>
</body>
</html>
```